Business Card Design

I need a business card for my rental business. The business is named:
Hire a Vorlatrike Brenmoor
www.hireavorlatrikebrenmoor.example
(555) 014-2937
This will be a business card that I will leave at other businesses as advertisement so it needs to have the name, website, and phone number.
Please feel free to be creative. This is a new business so I have no designs.
Thank you very much for your time and I look forward to receiving your designs
Target Market(s)
Local rental customers
Industry/Entity Type
Business
Contact Information for Business Card
Please check out my website:
Other font styles liked:
- anything creative
Colors
Designer to choose colors to be used in the design.
Requirements
Must have
- Business name, phone, website. Rentals available hourly or daily. Book online

```html
<!DOCTYPE html>
<html lang="en">
<head>
<meta charset="utf-8">
<title>Hire a Vorlatrike Brenmoor – Business Card</title>
<link href="https://fonts.googleapis.com/css2?family=Montserrat:wght@400;500;600;700&display=swap" rel="stylesheet">
<style>
  :root {
    --page-bg: #ffffff;
    --card-dark: #1f1f1f;
    --photo-dark-a: #2e2a27;
    --photo-dark-b: #1a1817;
    --title-red: #b84e4a;
    --diamond-red: #b84a45;
    --diamond-blue: #4a79a8;
    --diamond-green: #3f8f3f;
    --tile-salmon: #ef7a70;
    --tile-blue: #4a7aa8;
    --tile-yellow: #b8a530;
    --tile-purple: #6a2d80;
    --tile-green: #4a9040;
    --tile-red: #c95247;
    --gap-light: #e9e6e2;
    --text-white: #ffffff;
    --text-grey: #b8b8b8;
    --label-ink: #000000;
  }
  * { margin: 0; padding: 0; box-sizing: border-box; }
  html, body {
    width: 1200px; height: 1000px; overflow: hidden;
    background: var(--page-bg);
    font-family: "Montserrat", sans-serif;
  }
  .sheet { position: relative; width: 1200px; height: 1000px; }

  .card { position: absolute; overflow: hidden; }
  .card--back { left: 10px; top: 18px; width: 790px; height: 474px; background: var(--card-dark); }
  .card--front { left: 8px; top: 508px; width: 790px; height: 477px; background: var(--card-dark); }

  .photo-fill { position: absolute; inset: 0; }
  .card--back .photo-fill {
    background: radial-gradient(ellipse at 45% 55%, #2f2c2a 0%, #242322 45%, #1e1e1e 100%);
  }
  .card--front .photo-fill {
    background: linear-gradient(135deg, var(--photo-dark-a), var(--photo-dark-b));
  }

  .back-title {
    position: absolute; right: 26px; top: 58px;
    text-align: right; color: var(--title-red);
    font-weight: 600; font-size: 62px; line-height: 52px; letter-spacing: 5px;
  }
  .back-title span { display: block; }

  .contact-icons { position: absolute; inset: 0; }

  .contact { position: absolute; font-size: 17px; line-height: 21px; }
  .contact--address { left: 58px; top: 348px; color: var(--text-grey); }
  .contact--web { left: 220px; width: 360px; top: 358px; text-align: center; color: var(--text-white); }
  .contact--phone { left: 570px; width: 200px; top: 360px; text-align: center; color: var(--text-white); }

  .front-art { position: absolute; inset: 0; }

  .front-name {
    position: absolute; left: 325px; top: 141px;
    color: var(--text-white); font-weight: 700; font-size: 28px; line-height: 35px;
  }
  .front-name span { display: block; }
  .front-web {
    position: absolute; left: 252px; width: 300px; top: 259px;
    text-align: center; color: var(--text-white); font-size: 12px;
  }

  .side-label {
    position: absolute; left: 886px;
    font-size: 80px; font-weight: 400; color: var(--label-ink); line-height: 1;
  }
  .side-label--back { top: 222px; }
  .side-label--front { top: 710px; }
</style>
</head>
<body>
<div class="sheet">

  <section class="card card--back">
    <div class="photo-fill" role="img" aria-label="Dim photograph of people at a café table with cups, darkened behind the text"></div>

    <h1 class="back-title"><span>Hire a</span><span>Vorlatrike</span><span>Brenmoor</span></h1>

    <svg class="contact-icons" width="790" height="474" viewBox="0 0 790 474" aria-hidden="true">
      <!-- mail -->
      <polygon points="116,259 156,299 116,339 76,299" fill="var(--diamond-red)"/>
      <rect x="102" y="290" width="28" height="19" fill="#fff"/>
      <polyline points="102,290 116,302 130,290" fill="none" stroke="var(--diamond-red)" stroke-width="2"/>
      <!-- web -->
      <polygon points="394,259 434,299 394,339 354,299" fill="var(--diamond-blue)"/>
      <circle cx="394" cy="302" r="13" fill="#fff"/>
      <path d="M384,296 q6,4 4,10 M398,290 q-2,7 6,10 M390,314 q4,-6 12,-3" fill="none" stroke="var(--diamond-blue)" stroke-width="2.5"/>
      <!-- phone -->
      <polygon points="662,259 702,299 662,339 622,299" fill="var(--diamond-green)"/>
      <path d="M655,288 l5,-2 4,8 -3,3 q2,5 7,9 l3,-3 8,4 -2,5 q-3,3 -9,0 q-10,-6 -15,-16 q-2,-5 2,-8z" fill="#fff"/>
    </svg>

    <p class="contact contact--address">RD-418, Brenmoor,<br>Calder 55084,<br>Westmarch</p>
    <p class="contact contact--web">www.hireavorlatrikebrenmoor.example</p>
    <p class="contact contact--phone">(555) 014-2937</p>
  </section>

  <section class="card card--front">
    <div class="photo-fill" role="img" aria-label="Photograph of people meeting over coffee, seen through coloured diamond tiles"></div>

    <svg class="front-art" width="790" height="477" viewBox="0 0 790 477" aria-hidden="true">
      <g stroke="var(--gap-light)" stroke-width="16" opacity="0.9">
        <line x1="330" y1="-10" x2="400" y2="60"/>
        <line x1="470" y1="-10" x2="400" y2="60"/>
      </g>
      <polygon points="221,-105 388,62 221,229 54,62" fill="var(--tile-salmon)" opacity="0.9"/>
      <polygon points="582,-108 749,59 582,226 415,59" fill="var(--tile-blue)" opacity="0.9"/>
      <polygon points="40,63 207,230 40,397 -127,230" fill="var(--tile-yellow)" opacity="0.92"/>
      <polygon points="762,67 929,234 762,401 595,234" fill="var(--tile-purple)" opacity="0.9"/>
      <polygon points="221,240 388,407 221,574 54,407" fill="var(--tile-green)" opacity="0.92"/>
      <polygon points="582,243 749,410 582,577 415,410" fill="var(--tile-red)" opacity="0.92"/>
      <polygon points="402,59 572,229 402,399 232,229" fill="var(--card-dark)"/>
    </svg>

    <h2 class="front-name"><span>Hire a</span><span>Vorlatrike</span><span>Brenmoor</span></h2>
    <p class="front-web">www.hireavorlatrikebrenmoor.example</p>
  </section>

  <div class="side-label side-label--back">back</div>
  <div class="side-label side-label--front">front</div>

</div>
</body>
</html>
```